Grand Opening of Rusty's Tap, a craft beer bar in mountains of Payson AZ. Rusty is our black lab.

We need a card designed to advertise the grand opening of Rusty's Tap. It is a craft beer bar (we do not make our own beer but will highlight local beer) located next to Pinecrest Lanes (which has also been rebranded). We will be serving craft beer and spirited drinks, along with a great burger (Rusty's Melt) and other bar food. The interior is a little industrial (corregated metal bar front) with a warm feel. We are trying to appeal to a more upscale crowd without being snobby. We would like it to be family friendly during the day.

Reason: I'm extending the deadline by 1 day so I have time to review updates. Thank you all for submissions!

```html
<!DOCTYPE html>
<html lang="en">
<head>
<meta charset="utf-8">
<title>Rusty's Tap — Grand Opening</title>
<link href="https://fonts.googleapis.com/css2?family=Alike&family=Alegreya+Sans+SC:wght@500;700&family=Alegreya+SC:wght@500;700&display=swap" rel="stylesheet">
<style>
  :root {
    --wood-dark: #4a2c17;
    --wood-mid: #7a4e2d;
    --wood-light: #8f5f38;
    --metal-dark: #6e7378;
    --metal-light: #c9cdd1;
    --gold-dark: #9a6a1c;
    --gold: #d9a640;
    --gold-light: #f6dc94;
    --black: #151515;
    --black-soft: #3a3a3a;
    --cream: #fbf4e4;
    --white: #ffffff;
    --red-dark: #6e0a0a;
    --red: #c4161c;
    --wheat: #eee6c8;
  }
  * { margin: 0; padding: 0; box-sizing: border-box; }
  html, body { width: 1200px; height: 800px; overflow: hidden; background: var(--wood-dark); }
  .card {
    position: relative; width: 1200px; height: 800px; overflow: hidden;
    background: linear-gradient(90deg, var(--wood-dark), var(--wood-mid) 20%, var(--wood-light) 50%, var(--wood-mid) 80%, var(--wood-dark));
  }
  .metal-band {
    position: absolute; left: 0; width: 1200px;
    background: repeating-linear-gradient(180deg, var(--metal-light) 0 6px, var(--metal-dark) 6px 12px);
  }
  .metal-band--top { top: 0; height: 150px; }
  .metal-band--bottom { bottom: 0; height: 145px; }
  .wood-wall {
    position: absolute; left: 0; top: 150px; width: 1200px; height: 505px;
    background: linear-gradient(180deg, var(--wood-mid), var(--wood-light) 50%, var(--wood-mid));
  }
  .opening-plate {
    position: absolute; left: 285px; top: 28px; width: 630px; height: 152px;
    border-radius: 76px; padding: 8px;
    background: linear-gradient(180deg, var(--gold-light), var(--gold) 40%, var(--gold-dark));
  }
  .opening-plate__inner {
    width: 100%; height: 100%; border-radius: 70px;
    background: linear-gradient(180deg, var(--black-soft), var(--black) 60%);
    display: flex; align-items: center; justify-content: center;
    font-family: "Alegreya Sans SC", sans-serif; font-weight: 700;
    font-size: 78px; color: var(--white); letter-spacing: 1px;
  }
  .bar-name {
    position: absolute; left: 0; top: 180px; width: 1200px; text-align: center;
    font-family: "Alike", serif; font-size: 158px; line-height: 1; color: var(--white);
    text-shadow: 0 3px 6px rgba(0,0,0,.35);
  }
  .wheat {
    position: absolute; top: 340px; width: 140px; height: 310px;
    border-radius: 70px 70px 40px 40px;
    background: radial-gradient(ellipse at center, var(--wheat) 40%, var(--gold) 75%, transparent 76%);
  }
  .wheat--left { left: 60px; transform: rotate(-12deg); }
  .wheat--right { right: 60px; transform: rotate(12deg); }
  .date-ribbon { position: absolute; left: 340px; top: 362px; width: 520px; height: 150px; }
  .date-ribbon__text {
    position: absolute; left: 0; top: 30px; width: 520px; text-align: center;
    font-family: "Alegreya SC", serif; font-weight: 700; color: var(--white);
  }
  .date-ribbon__date { font-size: 44px; line-height: 1; display: block; }
  .date-ribbon__time { font-size: 24px; display: block; margin-left: 80px; }
  .lineup {
    position: absolute; left: 0; top: 512px; width: 1200px; text-align: center;
    font-family: "Alegreya SC", serif; font-weight: 500; font-size: 31px;
    line-height: 37px; color: var(--cream); text-shadow: 0 2px 4px rgba(0,0,0,.5);
  }
  .specials-pill {
    position: absolute; left: 390px; top: 678px; width: 416px; height: 98px;
    border-radius: 49px; padding: 6px;
    background: linear-gradient(180deg, var(--gold-light), var(--gold) 45%, var(--gold-dark));
  }
  .specials-pill__inner {
    width: 100%; height: 100%; border-radius: 44px;
    background: linear-gradient(90deg, var(--red-dark), var(--red) 50%, var(--red-dark));
    display: flex; flex-direction: column; align-items: center; justify-content: center;
    font-family: "Alegreya SC", serif; font-weight: 500; color: var(--white);
  }
  .specials-pill__main { font-size: 27px; line-height: 1.1; }
  .specials-pill__sub { font-size: 19px; }
  .burst { position: absolute; width: 210px; height: 210px; }
  .burst--left { left: 65px; top: 590px; }
  .burst--right { left: 925px; top: 605px; }
  .burst svg { position: absolute; inset: 0; }
  .burst__text {
    position: absolute; inset: 0; display: flex; align-items: center; justify-content: center;
    text-align: center; font-family: "Alegreya Sans SC", sans-serif; font-weight: 700;
    color: var(--white);
  }
  .burst--left .burst__text { font-size: 21px; line-height: 23px; }
  .burst--right .burst__text { font-size: 29px; line-height: 30px; }
</style>
</head>
<body>
<div class="card">
  <div class="wood-wall" role="img" aria-label="Warm wood plank wall texture"></div>
  <div class="metal-band metal-band--top" role="img" aria-label="Corrugated metal band"></div>
  <div class="metal-band metal-band--bottom" role="img" aria-label="Corrugated metal band"></div>

  <div class="opening-plate"><div class="opening-plate__inner">GRAND OPENING</div></div>

  <h1 class="bar-name">Rusty's Tap</h1>

  <div class="wheat wheat--left" role="img" aria-label="Golden wheat stalk ornament"></div>
  <div class="wheat wheat--right" role="img" aria-label="Golden wheat stalk ornament"></div>

  <div class="date-ribbon">
    <svg width="520" height="150" viewBox="0 0 520 150">
      <defs>
        <linearGradient id="ribbonGold" x1="0" y1="0" x2="0" y2="1">
          <stop offset="0" stop-color="#f6dc94"/><stop offset=".5" stop-color="#d9a640"/><stop offset="1" stop-color="#9a6a1c"/>
        </linearGradient>
      </defs>
      <polygon points="0,60 90,60 90,140 0,140 30,100" fill="#151515" stroke="url(#ribbonGold)" stroke-width="4"/>
      <polygon points="520,60 430,60 430,140 520,140 490,100" fill="#151515" stroke="url(#ribbonGold)" stroke-width="4"/>
      <polygon points="60,10 460,10 460,120 60,120" fill="#202020" stroke="url(#ribbonGold)" stroke-width="6"/>
    </svg>
    <div class="date-ribbon__text">
      <span class="date-ribbon__date">September 19th</span>
      <span class="date-ribbon__time">at 4pm.</span>
    </div>
  </div>

  <p class="lineup">
    Live entertainment by:<br>
    Ridge Five on Friday night<br>
    Dale Marcone &amp; the Hot Espressos<br>
    on Saturday night and Sunday afternoon.
  </p>

  <div class="specials-pill">
    <div class="specials-pill__inner">
      <span class="specials-pill__main">$3 Craft beers</span>
      <span class="specials-pill__sub">and drink specials all weekend</span>
    </div>
  </div>

  <div class="burst burst--left">
    <svg viewBox="-105 -105 210 210">
      <polygon fill="#d9a640" stroke="#f6dc94" stroke-width="2" points="100,0 79.2,21.2 86.6,50 58,58 50,86.6 21.2,79.2 0,100 -21.2,79.2 -50,86.6 -58,58 -86.6,50 -79.2,21.2 -100,0 -79.2,-21.2 -86.6,-50 -58,-58 -50,-86.6 -21.2,-79.2 0,-100 21.2,-79.2 50,-86.6 58,-58 86.6,-50 79.2,-21.2"/>
      <polygon transform="scale(.86)" fill="#2a2a2a" points="100,0 79.2,21.2 86.6,50 58,58 50,86.6 21.2,79.2 0,100 -21.2,79.2 -50,86.6 -58,58 -86.6,50 -79.2,21.2 -100,0 -79.2,-21.2 -86.6,-50 -58,-58 -50,-86.6 -21.2,-79.2 0,-100 21.2,-79.2 50,-86.6 58,-58 86.6,-50 79.2,-21.2"/>
    </svg>
    <div class="burst__text">Buy one<br>sandwich<br>get one 50%<br>off coupon</div>
  </div>

  <div class="burst burst--right">
    <svg viewBox="-105 -105 210 210">
      <polygon fill="#d9a640" stroke="#f6dc94" stroke-width="2" points="100,0 79.2,21.2 86.6,50 58,58 50,86.6 21.2,79.2 0,100 -21.2,79.2 -50,86.6 -58,58 -86.6,50 -79.2,21.2 -100,0 -79.2,-21.2 -86.6,-50 -58,-58 -50,-86.6 -21.2,-79.2 0,-100 21.2,-79.2 50,-86.6 58,-58 86.6,-50 79.2,-21.2"/>
      <polygon transform="scale(.86)" fill="#2a2a2a" points="100,0 79.2,21.2 86.6,50 58,58 50,86.6 21.2,79.2 0,100 -21.2,79.2 -50,86.6 -58,58 -86.6,50 -79.2,21.2 -100,0 -79.2,-21.2 -86.6,-50 -58,-58 -50,-86.6 -21.2,-79.2 0,-100 21.2,-79.2 50,-86.6 58,-58 86.6,-50 79.2,-21.2"/>
    </svg>
    <div class="burst__text">Great<br>burgers</div>
  </div>
</div>
</body>
</html>
```